Varga Lillas Physiotherapy Business Card Vienna

We need a business card design for a newly created Physiotherapy company based in Vienna Austria.
We seek a simple, modern, minimalist design without too much color variation. The font should look young/fresh, but definitely not childish or so. Since we are a starting Business, we currently haven't got a logo, if you feel like a logo would fit your design, feel free to use one, but it's not necessary.
Target Market(s)
Healthcare, young and elderly people with mobility issues
Industry/Entity Type
Health And Wellness
Contact Information for Business Card
Name: Lilla Varga
Title description: Physiotherapist
Phone num: +43 664 5290 4816
e-mail: lilla.praxis@brelomail.com
Colors
Designer to choose colors to be used in the design.
Requirements
Must have
- Final design language must be in German, basically, the Title Description needs to be "Physiotherapeutin" the other details remain as in the English Language.
Nice to have
- Simple, modern, minimalist design
Should not have
- too many colors, Obvious use of a skeleton, skull, spline

```html
<!DOCTYPE html>
<html lang="de">
<head>
<meta charset="utf-8">
<title>Lilla Varga – Visitenkarte</title>
<link rel="stylesheet" href="https://fonts.googleapis.com/css2?family=Fira+Sans+Condensed:wght@400&display=swap">
<style>
  :root {
    --backdrop: #e6e6e6;
    --card-dark: #1f1f1f;
    --card-light: #ffffff;
    --text-light: #ffffff;
    --text-dark: #1f1f1f;
  }
  html, body {
    margin: 0;
    padding: 0;
    width: 1200px;
    height: 1000px;
    overflow: hidden;
    background: var(--backdrop);
  }
  .canvas {
    position: relative;
    width: 1200px;
    height: 1000px;
  }
  .business-card {
    position: absolute;
    left: 120px;
    top: 200px;
    width: 960px;
    height: 600px;
    background: var(--card-dark);
    box-shadow: 0 6px 18px rgba(0, 0, 0, 0.35);
    overflow: hidden;
    font-family: "Fira Sans Condensed", "Arial Narrow", sans-serif;
  }
  .card-curve {
    position: absolute;
    inset: 0;
    width: 960px;
    height: 600px;
  }
  .brand-mark {
    position: absolute;
    right: 44px;
    top: 78px;
    display: flex;
    align-items: center;
    gap: 14px;
    color: var(--text-dark);
    font-size: 34px;
    font-weight: 400;
    line-height: 1;
  }
  .brand-dot {
    width: 30px;
    height: 30px;
    border: 3px solid var(--text-dark);
    border-radius: 50%;
    box-sizing: border-box;
  }
  .contact-block {
    position: absolute;
    left: 42px;
    top: 258px;
    margin: 0;
    color: var(--text-light);
    font-size: 55px;
    font-weight: 400;
    line-height: 71px;
    letter-spacing: -0.5px;
  }
  .contact-block span { display: block; }
</style>
</head>
<body>
  <main class="canvas">
    <section class="business-card" aria-label="Visitenkarte Lilla Varga">
      <svg class="card-curve" viewBox="0 0 960 600" aria-hidden="true">
        <path d="M430 0 L960 0 L960 600 C 930 300 720 70 430 0 Z" fill="var(--card-light)"/>
      </svg>
      <div class="brand-mark">
        <span class="brand-dot"></span>
        <span class="brand-name">Varga Lillas</span>
      </div>
      <p class="contact-block">
        <span class="contact-name">Lilla Varga</span>
        <span class="contact-title">Physiotherapeutin</span>
        <span class="contact-phone">+43 664 5290 4816</span>
        <span class="contact-email">lilla.praxis@brelomail.com</span>
      </p>
    </section>
  </main>
</body>
</html>
```